Power point template for corporate use

We need a simple power point template to use with our new logo design for corporate presentations to prospects

Target Market(s)

Corporate marketing departments - clients purchase our services and data

```html
<!DOCTYPE html>
<html lang="en">
<head>
<meta charset="utf-8">
<title>Corporate Presentation Template – Title Slide</title>
<link rel="stylesheet" href="https://fonts.googleapis.com/css2?family=PT+Sans:wght@400;700&display=swap">
<style>
  :root {
    --slide-bg: #ffffff;
    --title-red: #e3111b;
    --sub-grey: #9a9a9a;
    --brand-ink: #111111;
    --band-orange: #f47700;
    --band-rule: #111111;
    --header-tone-a: #fbe3ee;
    --header-tone-b: #fdf3d6;
    --header-tone-c: #dff1fb;
  }
  * { margin: 0; padding: 0; box-sizing: border-box; }
  html, body {
    width: 1200px;
    height: 901px;
    overflow: hidden;
    background: var(--slide-bg);
  }
  .slide {
    position: relative;
    width: 1200px;
    height: 901px;
    overflow: hidden;
    background: var(--slide-bg);
    font-family: "PT Sans", Arial, sans-serif;
  }
  .header-art {
    position: absolute;
    top: 0;
    left: 0;
    width: 1200px;
    height: 360px;
    background: linear-gradient(180deg,
      rgba(255,255,255,0) 0%,
      rgba(255,255,255,0) 70%,
      var(--slide-bg) 100%),
      linear-gradient(100deg,
      var(--header-tone-a) 0%,
      var(--header-tone-b) 50%,
      var(--header-tone-c) 100%);
  }
  .brand {
    position: absolute;
    left: 94px;
    top: 462px;
    width: 260px;
    color: var(--brand-ink);
    font-weight: 700;
  }
  .brand-name {
    display: block;
    font-size: 76px;
    line-height: 1;
    letter-spacing: -1px;
  }
  .brand-tagline {
    display: block;
    margin-top: 70px;
    font-size: 25px;
    line-height: 1;
    letter-spacing: 1.5px;
  }
  .title-block {
    position: absolute;
    left: 506px;
    top: 482px;
    width: 600px;
    text-align: center;
  }
  .project-title {
    color: var(--title-red);
    font-size: 67px;
    font-weight: 700;
    line-height: 1.1;
  }
  .project-sub {
    margin-top: 26px;
    color: var(--sub-grey);
    font-size: 32px;
    font-weight: 400;
    line-height: 41px;
  }
  .footer-rule {
    position: absolute;
    left: 0;
    top: 829px;
    width: 1200px;
    height: 6px;
    background: var(--band-rule);
  }
  .footer-band {
    position: absolute;
    left: 0;
    top: 835px;
    width: 1200px;
    height: 66px;
    background: var(--band-orange);
  }
</style>
</head>
<body>
  <main class="slide">
    <div class="header-art" role="img" aria-label="Decorative header artwork: colourful mosaic wave in pink, orange, yellow, green and blue"></div>

    <div class="brand">
      <span class="brand-name">ORVANE</span>
      <span class="brand-tagline">DIGITAL MARKETING</span>
    </div>

    <section class="title-block">
      <h1 class="project-title">Project Title Here</h1>
      <p class="project-sub">Sub Content here, Sub Content here<br>Sub Content here</p>
    </section>

    <div class="footer-rule"></div>
    <div class="footer-band"></div>
  </main>
</body>
</html>
```